A new presentation to our clients

we are a Real Estate agency, our website is www.dorelumia.com and it’s time to have a new, fashion and remarcable Business Card. we want to differentiate ourselves from other companies so we want a business card that differentiates us. we want the business card to impact our customers. in the competitive market that we have today, we have to be different and it is this difference that we seek

Target Market(s)

Real Estate Clients

Contact Information for Business Card

We search a totaly diferent card from the usual

Font styles to use
Sans Serif

Colors
e34197

Requirements
Must have
• Logo, adress, phone contact, e-mail, photo, and our website
Nice to have
• We would like to see a modern business card
Should not have
• Houses or building draws

```html
<!DOCTYPE html>
<html lang="en">
<head>
<meta charset="utf-8">
<title>Dore Lumia — Business Card</title>
<link rel="stylesheet" href="https://fonts.googleapis.com/css2?family=PT+Sans:wght@400;700&display=swap">
<style>
  :root {
    --brand-pink: #e34197;
    --card-white: #ffffff;
    --text-white: #ffffff;
    --photo-dark: #4a4448;
    --photo-mid: #6b5e63;
    --photo-blush: #8a5a66;
  }
  * { margin: 0; padding: 0; box-sizing: border-box; }
  html, body {
    width: 1200px;
    height: 694px;
    overflow: hidden;
    background: var(--card-white);
  }
  .card {
    position: relative;
    width: 1200px;
    height: 694px;
    overflow: hidden;
    font-family: "PT Sans", sans-serif;
  }
  .card__photo {
    position: absolute;
    left: 0;
    top: 0;
    width: 1045px;
    height: 694px;
    background:
      radial-gradient(ellipse at 82% 22%, rgba(160, 80, 100, 0.55), transparent 45%),
      radial-gradient(ellipse at 30% 80%, rgba(150, 70, 90, 0.45), transparent 40%),
      radial-gradient(ellipse at 10% 10%, rgba(140, 120, 125, 0.5), transparent 50%),
      linear-gradient(135deg, var(--photo-mid) 0%, var(--photo-dark) 55%, var(--photo-blush) 100%);
  }
  .card__brand-strip {
    position: absolute;
    left: 1045px;
    top: 0;
    width: 155px;
    height: 694px;
    background: var(--card-white);
    display: flex;
    align-items: center;
    justify-content: center;
  }
  .brand-name {
    writing-mode: vertical-rl;
    font-size: 104px;
    font-weight: 700;
    line-height: 1;
    color: var(--brand-pink);
    white-space: nowrap;
  }
  .contact-line {
    position: absolute;
    left: 29px;
    font-size: 51px;
    font-weight: 400;
    line-height: 1;
    color: var(--text-white);
    white-space: nowrap;
  }
  .contact-line--website { top: 59px; }
  .contact-line--email { top: 159px; }
  .contact-line--address-1 { top: 263px; }
  .contact-line--address-2 { top: 339px; }
  .contact-line--address-3 { top: 416px; }
  .contact-line--address-4 { top: 491px; }
  .contact-line--phone { top: 578px; }
</style>
</head>
<body>
  <main class="card">
    <div class="card__photo" role="img" aria-label="Soft-focus photograph of bare branches with small pink blossoms"></div>

    <p class="contact-line contact-line--website">Website: www.dorelumia.com</p>
    <p class="contact-line contact-line--email">Email: geral@dorelumia.com</p>
    <p class="contact-line contact-line--address-1">Address: Av. Lumiar</p>
    <p class="contact-line contact-line--address-2">S. Tavares,</p>
    <p class="contact-line contact-line--address-3">148 4400-512, Vila Nova de</p>
    <p class="contact-line contact-line--address-4">Gaia</p>
    <p class="contact-line contact-line--phone">Telephone: (+351) 220 418 936</p>

    <aside class="card__brand-strip">
      <span class="brand-name">Dore Lumia</span>
    </aside>
  </main>
</body>
</html>
```